Church needs a graphic design/flyer layout for upcoming series

I need a multi-purpose design for promoting both our upcoming series of messages and our fall kick-off event where we will launch the messages.

Our promotion will be printed on a two-sided. One side is simple and focuses on the series and the other side has details in regards to the event. I have provided an attachment example of what we did last time.

The design needs to be multi-purpose because it will be used for our sermon Power Points, placed on our website banner, social media, etc.

• Sermon series is called “Harbor Lanterns”
• The subtitle will be “What’s keeping you from God?”
• Our name logo should be on the graphic as well.
• The subject manner will revolve around common hurdles that people face about God and Christianity: The existence of God, the exclusivity of religion, Hell, the reliability of the Bible, Hypocrisy in the church, etc.
• Our mission is “Connecting Young Families to Christ” so our focus is to reach out to families while not being exclusive to others.
• Our target audience is families with school-aged kids.
• This series is an invitational focus so we want it to be appealing to non-church goers.
• It should be attention grabbing while not being too ‘edgy’

• The front of the card will most likely consist the Sermon Series Graphic, title & subtitle of the series, and perhaps our name logo somewhere on it.
• The back of the card will invite and give the basic information for the event so that the people will be encouraged to save the date and come to the event.
• Here are some things that could be included on that advertisement:
o The name of the event: “Westbrook Commons Open Day”
o The date and time of the event: Sept 23rd @ 10:30
o Features of the event:
 Free lunch
 Children’s program
 Bouncy Castle
 Start of the “Harbor Lanterns” messages.
 Sample of topics
o Information about the church: our website and address, etc
o Engaging pictures and graphics.
• The rest of the tone and manner are the same as the sermon series graphic.
The flyer will be 11X14, like a postcard size.

Target Market(s)

Young families who are spiritually curious but not committed church attenders.

Colors

Designer to choose colors to be used in the design.

Requirements
Nice to have
• A modern and professional looking design.
Should not have
• Anything offensive or not family friendly.

```html
<!DOCTYPE html>
<html lang="en">
<head>
<meta charset="utf-8">
<title>Harbor Lanterns – Westbrook Commons Open Day</title>
<link rel="stylesheet" href="https://fonts.googleapis.com/css2?family=Open+Sans:wght@400;600&family=Quicksand:wght@400;500&family=Great+Vibes&display=swap">
<style>
  :root{
    --page:#ffffff;
    --ink-dark:#3a3a3c;
    --ink-kicker:#5a5550;
    --gold:#e2c77f;
    --violet:#5b4a9e;
    --cyan:#27a9e1;
    --navy:#1f4e8c;
    --purple:#7a63b8;
    --red:#e8343a;
    --teal:#1aab8a;
    --blue:#2a7cc2;
    --band-top:#27a9e1;
    --band-mid:#1a8a78;
    --band-low:#3a5a8a;
    --band-base:#a795d4;
    --brand:#5f3d9a;
    --footer-ink:#3d3d3d;
    --border:#e6e6e6;
  }
  *{box-sizing:border-box;margin:0;padding:0}
  html,body{width:1200px;height:1200px;overflow:hidden;background:var(--page)}
  body{position:relative;font-family:"Open Sans",sans-serif}

  /* ---------- Series card (front) ---------- */
  .series-card{
    position:absolute;left:298px;top:91px;width:604px;height:474px;overflow:hidden;
  }
  .series-card__scene{
    position:absolute;inset:0;
    background:
      radial-gradient(ellipse 120px 200px at 50% 52%, rgba(255,250,235,1) 0%, rgba(255,245,225,.6) 40%, rgba(255,255,255,0) 100%),
      linear-gradient(180deg,#d4d6db 0%,#eef0f3 30%,#f4f4f2 50%,#6b6c70 62%,#2b2b2d 80%,#050505 100%);
  }
  .series-card__brand{
    position:absolute;top:26px;left:0;right:0;text-align:center;
    font-size:7px;color:#333;letter-spacing:.2px;
  }
  .series-card__brand .brand-dot{
    display:block;width:34px;height:34px;border-radius:50%;
    background:var(--brand);margin:0 auto 4px;
  }
  .series-card__kicker{
    position:absolute;top:96px;left:0;right:0;text-align:center;
    font-size:66px;letter-spacing:30px;padding-left:30px;
    color:var(--ink-kicker);font-weight:400;line-height:1;
  }
  .series-card__title{
    position:absolute;top:183px;left:0;right:0;text-align:center;
    font-size:98px;letter-spacing:-3px;color:var(--ink-dark);
    font-weight:400;line-height:1;
  }
  .series-card__subtitle{
    position:absolute;top:292px;left:0;right:0;text-align:center;
    font-family:"Great Vibes",cursive;font-size:33px;color:var(--gold);
  }

  /* ---------- Event card (back) ---------- */
  .event-card{
    position:absolute;left:298px;top:665px;width:606px;height:475px;
    border:2px solid var(--border);overflow:hidden;background:#fff;
  }
  .event-card__title{
    position:absolute;top:30px;left:0;right:0;text-align:center;
    font-family:"Quicksand",sans-serif;font-weight:400;color:var(--violet);font-size:29px;line-height:1;
  }
  .event-card__title .emphasis{font-size:36px}
  .event-card__date{
    position:absolute;top:76px;left:0;right:0;text-align:center;
    font-family:"Quicksand",sans-serif;color:var(--cyan);font-size:18px;
  }
  .features{
    position:absolute;top:106px;left:0;right:0;display:flex;justify-content:center;gap:22px;
    list-style:none;
  }
  .feature{width:46px;text-align:center;font-family:"Quicksand",sans-serif;font-size:11.5px;line-height:1.05}
  .feature svg{display:block;margin:0 auto 4px;width:38px;height:38px}
  .feature--lunch{color:var(--navy)}
  .feature--kids{color:var(--purple)}
  .feature--castle{color:var(--red)}
  .feature--series{color:var(--teal)}
  .feature--topics{color:var(--blue)}

  .photo-strip{position:absolute;top:184px;left:0;width:602px;height:104px}
  .photo{position:absolute;top:0;height:104px}
  .photo--couple{left:0;width:144px;background:linear-gradient(135deg,#c9c9c9,#8d8d8d)}
  .photo--splash{left:150px;width:146px;background:linear-gradient(180deg,#dcdcdc,#7a7a7a)}
  .photo--embrace{left:303px;width:147px;background:linear-gradient(135deg,#f0f0f0,#6e6e6e)}
  .photo--bible{left:456px;width:146px;background:linear-gradient(135deg,#3a3a3a,#9a9a9a)}

  .colour-band{
    position:absolute;top:301px;left:0;width:602px;height:82px;
    background:linear-gradient(180deg,var(--band-top) 0%,var(--band-mid) 35%,var(--band-low) 75%,var(--band-base) 100%);
  }

  .event-footer{
    position:absolute;top:404px;left:0;right:0;font-size:11.5px;color:var(--footer-ink);
    line-height:15px;letter-spacing:.3px;
  }
  .event-footer__address{position:absolute;left:24px;font-style:normal}
  .event-footer__contact{position:absolute;left:217px}
  .event-footer__brand{position:absolute;left:478px;top:-2px;width:118px;text-align:center;font-size:8px;color:#333}
  .event-footer__brand .brand-dot{display:block;width:40px;height:40px;border-radius:50%;background:var(--brand);margin:0 auto 4px}
</style>
</head>
<body>

<section class="series-card">
  <div class="series-card__scene" role="img" aria-label="Photo of a figure standing on a rocky hill in bright backlight, fading to dark foreground"></div>
  <div class="series-card__brand"><span class="brand-dot"></span>Maple Hollow Family Church</div>
  <div class="series-card__kicker">HARBOR</div>
  <h1 class="series-card__title">LANTERNS</h1>
  <p class="series-card__subtitle">What's keeping you from God?</p>
</section>

<section class="event-card">
  <h2 class="event-card__title">Westbrook Commons <span class="emphasis">Open Day</span></h2>
  <p class="event-card__date">Sept 23rd 2018 @ 10:30</p>

  <ul class="features">
    <li class="feature feature--lunch">
      <svg viewBox="0 0 38 38"><circle cx="19" cy="19" r="17" fill="#fff" stroke="#1f4e8c" stroke-width="3"/><circle cx="19" cy="19" r="13" fill="#1f4e8c"/><path d="M15 11v16M13 11v5h4v-5M22 11c3 0 3 6 0 7v9" stroke="#e8772e" stroke-width="2" fill="none"/></svg>
      Free lunch
    </li>
    <li class="feature feature--kids">
      <svg viewBox="0 0 38 38"><circle cx="19" cy="19" r="18" fill="#7a63b8"/><circle cx="13" cy="12" r="3.5" fill="#fff"/><circle cx="25" cy="12" r="3.5" fill="#fff"/><path d="M9 17h8v9h-2v5h-4v-5H9zM21 17h8l1 9h-2v5h-4v-5h-2z" fill="#fff"/></svg>
      Children’s program
    </li>
    <li class="feature feature--castle">
      <svg viewBox="0 0 38 38"><rect x="3" y="8" width="32" height="28" rx="3" fill="#e8343a"/><rect x="9" y="16" width="20" height="14" fill="#f6c21c"/><rect x="14" y="22" width="10" height="8" fill="#2a7cc2"/></svg>
      Bouncy Castle
    </li>
    <li class="feature feature--series">
      <svg viewBox="0 0 38 38"><circle cx="19" cy="19" r="18" fill="#1aab8a"/><path d="M10 16h4l6-5v16l-6-5h-4z" fill="#fff"/><path d="M23 15c2 2 2 6 0 8M26 12c4 4 4 10 0 14" stroke="#fff" stroke-width="2" fill="none"/></svg>
      Harbor Lanterns
    </li>
    <li class="feature feature--topics">
      <svg viewBox="0 0 38 38"><circle cx="19" cy="19" r="18" fill="#2a7cc2"/><rect x="8" y="11" width="15" height="10" rx="2" fill="#fff"/><path d="M11 21l-1 4 5-4z" fill="#fff"/><rect x="16" y="16" width="15" height="10" rx="2" fill="#fff" stroke="#2a7cc2" stroke-width="1.5"/><path d="M27 26l1 4-5-4z" fill="#fff"/></svg>
      Sample of topics
    </li>
  </ul>

  <div class="photo-strip">
    <div class="photo photo--couple" role="img" aria-label="Black and white photo of a smiling couple outdoors"></div>
    <div class="photo photo--splash" role="img" aria-label="Black and white photo of a child kicking up water"></div>
    <div class="photo photo--embrace" role="img" aria-label="Black and white photo of a laughing couple embracing"></div>
    <div class="photo photo--bible" role="img" aria-label="Black and white photo of hands folded on an open Bible"></div>
  </div>

  <div class="colour-band" role="img" aria-label="Decorative band of layered blue, green and purple stripes"></div>

  <footer class="event-footer">
    <address class="event-footer__address">118 Orchard Lane West,<br>Riverton.<br>ON K2B 4X7</address>
    <div class="event-footer__contact">info@maplehollowchurch.ca<br>www.maplehollowchurch.ca<br>555 010 4821</div>
    <div class="event-footer__brand"><span class="brand-dot"></span>Maple Hollow Family Church</div>
  </footer>
</section>

</body>
</html>
```